Shopping Web Site

I am looking for a retail website for my Curry Powder Business, I only sell 3 or 4 items so just need a simple website design with checkout but colours are important as I need Indian orange, red, green colours, we will email more info to the successful party. Attached is our logo and you can Facebook Rovin Pantry to get more information. Thanks

Industry/Entity Type

Business

```html
<!DOCTYPE html>
<html lang="en">
<head>
<meta charset="utf-8">
<title>Rovin Pantry</title>
<link href="https://fonts.googleapis.com/css2?family=Roboto:wght@300;400;500&family=Lobster&display=swap" rel="stylesheet">
<style>
:root{
  --page:#f7efd6;
  --gold:#e9b65a;
  --gold-dark:#c9913a;
  --ink:#333;
  --muted:#666;
  --red:#d0281c;
  --white:#fff;
  --footer:#1f1f1f;
  --hero-dark:#3b3836;
}
*{margin:0;padding:0;box-sizing:border-box}
html,body{width:766px;height:1200px;overflow:hidden}
body{background:var(--page);font-family:'Roboto',sans-serif;color:var(--ink);position:relative}
.abs{position:absolute}

.basket-icon{left:62px;top:45px;width:26px;height:26px;border-radius:50%;background:#efe6cc}
.basket-icon svg{position:absolute;left:7px;top:7px}
.basket-label{left:94px;top:45px;font-size:8px;line-height:13px;color:var(--ink)}
.basket-label .count{display:block;margin-top:3px}

.brand{left:323px;top:14px;width:120px;text-align:center}
.brand-mark{width:58px;height:58px;border-radius:50%;border:2px solid var(--ink);margin:0 auto 6px}
.brand-name{font-size:12px;font-weight:500;color:var(--ink);letter-spacing:.5px}

.search{left:568px;top:46px;width:134px;height:25px;background:var(--white);border-radius:2px;font-size:7px;padding:9px 9px;color:var(--ink)}
.search svg{position:absolute;right:8px;top:8px}

.frame{left:64px;top:118px;width:638px;height:352px;border-radius:10px;background:var(--white);box-shadow:0 18px 18px -14px rgba(0,0,0,.35);padding:2px;overflow:hidden}
.nav{height:36px;background:linear-gradient(#eec06a,var(--gold));border-radius:8px 8px 0 0;position:relative}
.nav a{position:absolute;top:13px;font-size:9px;color:var(--white);text-decoration:none;text-transform:uppercase}
.hero{position:absolute;left:2px;top:38px;width:634px;height:312px;border-radius:0 0 8px 8px;overflow:hidden;
  background:linear-gradient(100deg,#7a4a28 0%,#9a3a22 22%,#5a4a3e 42%,var(--hero-dark) 60%,#353231 100%)}
.hero-title{left:376px;top:64px;font-family:'Lobster',cursive;font-size:42px;color:var(--gold);line-height:1;white-space:nowrap}
.hero-text{left:380px;top:134px;width:210px;font-size:8.5px;line-height:14px;color:var(--white)}
.hero-btn{left:380px;top:188px;width:84px;height:29px;background:var(--gold);border:1px solid #f3d08f;border-radius:3px;color:var(--white);font-size:9.5px;text-align:center;line-height:27px}
.hero-wave{left:0;bottom:0}
.dots{left:298px;top:296px;display:flex;gap:5px;align-items:center}
.dots span{width:6px;height:6px;border-radius:50%;background:#444}
.dots .on{width:9px;height:9px;background:var(--gold);border:2px solid #f5dca8}

.section-title{left:62px;top:500px;font-size:17px;color:var(--ink);font-weight:400}
.arrows{left:670px;top:503px;display:flex;gap:2px}
.arrows span{width:15px;height:15px;background:#555;color:var(--white);font-size:9px;text-align:center;line-height:15px}

.card{top:536px;width:149px;height:237px;background:var(--white);border:1px solid #ece5d2;text-align:center}
.card-photo{height:149px;background:linear-gradient(#fff,#f4f4f4);position:relative}
.card-ring{position:absolute;left:24px;top:20px;width:100px;height:100px;border-radius:50%;border:3px solid var(--gold)}
.card-title{margin-top:19px;font-size:10px;color:var(--ink)}
.card-desc{margin-top:7px;font-size:7.5px;line-height:13px;color:var(--muted)}
.card-link{margin-top:7px;font-size:7.5px;color:var(--red)}

.offers{left:64px;top:798px;width:638px;height:120px;border-radius:8px;border:2px solid var(--white);
  background:linear-gradient(90deg,#3a2418,#2f2a24 30%,#3a3020 55%,#2e2418 80%,#3a1a14);overflow:hidden}
.offer{top:28px;width:150px;text-align:center;color:var(--white)}
.offer-title{font-size:16px;font-weight:300;line-height:20px;text-transform:uppercase}
.offer-sub{margin-top:10px;font-size:9px}
.offer-line{width:40px;height:2px;background:var(--gold);margin:14px auto 0}

.cookbook{left:63px;top:948px;width:127px;height:170px;border-radius:8px;background:linear-gradient(160deg,#3a2a22,#7a3a1e 60%,#b0502a)}
.welcome-title{left:208px;top:942px;font-size:22px;font-weight:400;color:var(--ink)}
.welcome-title em{font-style:normal;color:var(--gold)}
.welcome-sub{left:209px;top:976px;font-size:9.5px;color:var(--ink)}
.welcome-text{left:209px;top:998px;width:262px;font-size:7px;line-height:13.2px;color:var(--muted)}
.welcome-btn{left:209px;top:1092px;width:125px;height:26px;background:var(--gold);color:var(--white);font-size:9.5px;text-align:center;line-height:26px;border-radius:2px}
.kitchen{left:495px;top:948px;width:208px;height:170px;border-radius:8px;background:linear-gradient(120deg,#e8e4de,#cfc6b8 40%,#8a5a32 70%,#d8d2c8)}

.footer{left:63px;top:1146px;width:640px;height:54px;background:var(--footer);border-radius:8px 8px 0 0;color:var(--white)}
.footer h4{font-size:12px;font-weight:400;text-transform:uppercase}
.footer p{font-size:7.5px;margin-top:4px}
.f-copy{left:17px;top:17px}
.f-contact{left:269px;top:17px}
.f-follow{left:477px;top:20px;display:flex;align-items:center;gap:12px}
.f-follow .icons{display:flex;gap:3px}
.f-follow .icons span{width:16px;height:16px;background:var(--white);border-radius:3px}
</style>
</head>
<body>

<div class="abs basket-icon">
  <svg width="12" height="12" viewBox="0 0 12 12"><path d="M0 1h2l2 6h6l1.5-4.5H3" fill="none" stroke="#888" stroke-width="1.4"/><circle cx="4.5" cy="10" r="1" fill="#888"/><circle cx="9" cy="10" r="1" fill="#888"/></svg>
</div>
<div class="abs basket-label">SHOPPING BASKET<span class="count">0 ITEM(S) - $0.00</span></div>

<div class="abs brand">
  <div class="brand-mark"></div>
  <div class="brand-name">Rovin Pantry</div>
</div>

<div class="abs search">SEARCH
  <svg width="8" height="8" viewBox="0 0 8 8"><circle cx="3.2" cy="3.2" r="2.4" fill="none" stroke="#222" stroke-width="1.2"/><path d="M5 5l2.5 2.5" stroke="#222" stroke-width="1.4"/></svg>
</div>

<div class="abs frame">
  <nav class="nav">
    <a style="left:26px">Home</a>
    <a style="left:94px">About Us</a>
    <a style="left:174px">Our Store</a>
    <a style="left:263px">Products</a>
    <a style="left:349px">Spices</a>
    <a style="left:426px">Checkout</a>
    <a style="left:514px">Contact Us</a>
  </nav>
  <div class="hero" role="img" aria-label="Wooden spoons holding cardamom pods, cloves and dried red chillies on a dark stone surface with bay leaves">
    <div class="abs hero-title">Rovin Pantry</div>
    <p class="abs hero-text">Sed purus purus, tincidunt eget malesuada et, moles ut eros. Fusce blandit. Sed purus purus, tincidunt eget malesuada</p>
    <div class="abs hero-btn">LEARN MORE</div>
    <svg class="abs hero-wave" width="634" height="30" viewBox="0 0 634 30"><path d="M0 30 L240 30 C262 30 272 8 320 8 C368 8 378 30 400 30 L634 30 Z" fill="#fff"/></svg>
    <div class="abs dots"><span class="on"></span><span></span><span></span><span></span></div>
  </div>
</div>

<h2 class="abs section-title">Rovin Pantry Products</h2>
<div class="abs arrows"><span>‹</span><span>›</span></div>

<div class="abs card" style="left:62px">
  <div class="card-photo" role="img" aria-label="Red chilli pepper on a heap of chilli powder"><div class="card-ring" style="background:radial-gradient(circle,#e04a30 0%,#fff 60%)"></div></div>
  <div class="card-title">SWEET PAPRIKA</div>
  <div class="card-desc">Lorem ipsum dolor sit amet,<br>consectetur adipiscing</div>
  <div class="card-link">SHOP NOW</div>
</div>
<div class="abs card" style="left:226px">
  <div class="card-photo" role="img" aria-label="Mound of ground brown spice with whole nutmeg"><div class="card-ring" style="background:radial-gradient(circle,#9a7a4a 0%,#fff 60%)"></div></div>
  <div class="card-title">SWEET PAPRIKA</div>
  <div class="card-desc">Lorem ipsum dolor sit amet,<br>consectetur adipiscing</div>
  <div class="card-link">SHOP NOW</div>
</div>
<div class="abs card" style="left:390px">
  <div class="card-photo" role="img" aria-label="Red bell pepper beside orange paprika powder"><div class="card-ring" style="background:radial-gradient(circle,#e8602a 0%,#fff 60%)"></div></div>
  <div class="card-title">SWEET PAPRIKA</div>
  <div class="card-desc">Lorem ipsum dolor sit amet,<br>consectetur adipiscing</div>
  <div class="card-link">SHOP NOW</div>
</div>
<div class="abs card" style="left:554px">
  <div class="card-photo" role="img" aria-label="Tomato, onion and peppercorns with a wooden scoop"><div class="card-ring" style="background:radial-gradient(circle,#c87a4a 0%,#fff 60%)"></div></div>
  <div class="card-title">SWEET PAPRIKA</div>
  <div class="card-desc">Lorem ipsum dolor sit amet,<br>consectetur adipiscing</div>
  <div class="card-link">SHOP NOW</div>
</div>

<div class="abs offers" role="img" aria-label="Dark background of chilli powder, peppercorns, star anise and curry leaves">
  <div class="abs offer" style="left:52px"><div class="offer-title">Chili<br>Powder</div><div class="offer-sub">GET UP TO 50% OFF</div><div class="offer-line"></div></div>
  <div class="abs offer" style="left:241px"><div class="offer-title">Spices<br>&amp; Herbs</div><div class="offer-sub">GET UP TO 50% OFF</div><div class="offer-line"></div></div>
  <div class="abs offer" style="left:446px"><div class="offer-title">Rovin<br>Pantry</div><div class="offer-sub">GET UP TO 50% OFF</div><div class="offer-line"></div></div>
</div>

<div class="abs cookbook" role="img" aria-label="Open cookbook and booklet on a patterned table cloth"></div>
<h2 class="abs welcome-title">Welcome to <em>Rovin Pantry</em></h2>
<div class="abs welcome-sub">Rovin Pantry Authentic Cook Book</div>
<p class="abs welcome-text">Lorem ipsum dolor sit amet, consectetur adipiscing elit, sed do eiusmod tempor incididunt ut labore et dolore magna aliqua. Ut enim ad minim veniam, quis nostrud exercitation ullamco laboris nisi ut aliquip ex ea commodo consequat. Duis aute irure dolor in reprehenderit in voluptate velit esse cillum dolore eu fugiat nulla pariatur. Excepteur sint occaecat cupidatat non proident, sunt in culpa qui officia deserunt mollit anim id est laborum.</p>
<div class="abs welcome-btn">MORE INFORMATION</div>
<div class="abs kitchen" role="img" aria-label="Mortar and pestle, herbs, lemon and a glass bowl of chicken on a wooden board"></div>

<footer class="abs footer">
  <div class="abs f-copy"><h4>Copyright</h4><p>(c) 2015 Rovin Pantry All rights reserved.</p></div>
  <div class="abs f-contact"><h4>Contact Us Today!</h4><p>+61 1300 555 018</p></div>
  <div class="abs f-follow"><h4>Follow Us</h4><div class="icons"><span></span><span></span><span></span></div></div>
</footer>

</body>
</html>
```